Card design for Heating and Cooling company

this is for a heating and cooling company we recently updated our logo and need to update our cards. We attached our logo so you can incorporate it into the card. We specialize in residential and commercial furnace and air condition repairs. Have been in business since 2014.

Phone number 555.284.9137

We need the following phrases
:Repairs, Installations, and maintenance
:Quality work at reasonable prices
:residential/commercial
:Licensed &Insured
:Email Pinegrovehvac47@mailbox-example.com
Name: Teodor K (Ted)
Also on back side I would like my logo with wording :Thank you for your business and refferal

Industry/Entity Type

Hvac

Contact Information for Business Card

:residential/commercial
:Licensed & Insured
Name: Teodor K (Ted)
Number:555.284.9136

Requirements
Must have
• Blue and red colors
Nice to have
• Maybe a pic of a furnace or air conditioner

```html
<!DOCTYPE html>
<html lang="en">
<head>
<meta charset="utf-8">
<title>Pinegrove Heating &amp; Cooling — Business Cards</title>
<link rel="stylesheet" href="https://fonts.googleapis.com/css2?family=Arimo:wght@400;700&display=swap">
<style>
  :root {
    --bg: #e9e7e4;
    --charcoal: #2f3134;
    --charcoal-deep: #232427;
    --silver: #b9bbbe;
    --silver-light: #dcdde0;
    --red: #d3202a;
    --red-dark: #8e1016;
    --white: #ffffff;
    --brand-blue: #1b8ed6;
    --text-light: #f2f2f2;
  }
  * { box-sizing: border-box; margin: 0; padding: 0; }
  html, body {
    width: 1200px; height: 901px; overflow: hidden;
    background: var(--bg);
    font-family: "Arimo", Arial, sans-serif;
  }
  .card {
    position: absolute; left: 240px;
    width: 720px; height: 411px;
    overflow: hidden;
    box-shadow: 0 10px 28px rgba(0,0,0,.25);
  }
  .card-back { top: 30px; background: var(--charcoal); }
  .card-front { top: 466px; background: var(--white); }
  .card svg.art { position: absolute; inset: 0; width: 100%; height: 100%; }

  /* back */
  .back-badge {
    position: absolute; left: 285px; top: 34px;
    width: 150px; height: 150px; border-radius: 50%;
    background: var(--white);
    display: flex; align-items: center; justify-content: center;
  }
  .brand-name {
    font-weight: 700; color: var(--brand-blue);
    letter-spacing: .5px;
  }
  .back-badge .brand-name { font-size: 24px; }
  .back-thanks {
    position: absolute; left: 0; right: 0; top: 318px;
    text-align: center; color: var(--text-light);
    font-size: 27px; letter-spacing: .5px;
  }

  /* front */
  .holder-name {
    position: absolute; left: 46px; top: 36px;
    color: var(--red); font-size: 25px;
  }
  .rule { position: absolute; left: 44px; width: 300px; height: 1px; background: #8a8c90; }
  .services {
    position: absolute; left: 44px; top: 92px;
    list-style: none; color: var(--text-light); font-size: 14px; line-height: 22px;
  }
  .services li { display: flex; align-items: center; gap: 8px; }
  .services li::before {
    content: ""; width: 9px; height: 9px; background: var(--red);
    transform: rotate(45deg); flex: none;
  }
  .contact {
    position: absolute; left: 44px; display: flex; align-items: center; gap: 10px;
    color: var(--text-light); font-size: 18px;
  }
  .contact-phone { top: 220px; }
  .contact-email { top: 272px; font-size: 16px; }
  .contact svg { width: 22px; height: 22px; flex: none; }
  .photo {
    position: absolute; width: 96px; height: 96px; border-radius: 50%;
    border: 3px solid var(--white);
    box-shadow: 0 0 0 2px var(--silver);
  }
  .photo-repair { left: 398px; top: 68px; background: linear-gradient(135deg, #e9eef2, #9fb3c2); }
  .photo-unit { left: 392px; top: 186px; background: linear-gradient(135deg, #cfe4f2, #f4f7f9 60%, #b8c4cc); }
  .front-logo {
    position: absolute; left: 548px; top: 224px;
    display: flex; align-items: center; gap: 8px;
  }
  .front-logo .mark { width: 20px; height: 20px; border-radius: 50%; background: var(--brand-blue); }
  .front-logo .brand-name { font-size: 20px; }
</style>
</head>
<body>

<section class="card card-back" aria-label="Business card, back">
  <svg class="art" viewBox="0 0 720 411" preserveAspectRatio="none" aria-hidden="true">
    <rect x="0" y="0" width="720" height="14" fill="var(--silver)"/>
    <rect x="0" y="397" width="720" height="14" fill="var(--silver)"/>
    <path d="M0 250 C200 215 420 150 720 120 L720 150 C430 175 220 240 0 290 Z" fill="var(--silver-light)"/>
    <path d="M0 268 C210 228 430 168 720 140 L720 182 C440 200 230 262 0 312 Z" fill="var(--red)"/>
    <path d="M0 300 C220 258 440 196 720 172 L720 186 C440 208 230 270 0 318 Z" fill="var(--red-dark)"/>
    <path d="M0 312 C230 270 450 214 720 190 L720 200 C450 226 240 284 0 330 Z" fill="var(--white)"/>
    <path d="M0 228 C180 205 380 185 560 172 C420 190 230 222 0 262 Z" fill="#55585c"/>
  </svg>
  <div class="back-badge"><span class="brand-name">PINEGROVE</span></div>
  <p class="back-thanks">Thank you for your business and refferal</p>
</section>

<section class="card card-front" aria-label="Business card, front">
  <svg class="art" viewBox="0 0 720 411" preserveAspectRatio="none" aria-hidden="true">
    <path d="M0 0 L470 0 C430 120 460 260 520 411 L0 411 Z" fill="var(--charcoal)"/>
    <path d="M470 0 L500 0 C470 130 500 270 560 411 L520 411 C460 260 430 120 470 0 Z" fill="#6f7276"/>
    <path d="M500 0 L535 0 C505 140 535 280 600 411 L560 411 C500 270 470 130 500 0 Z" fill="var(--red)"/>
    <path d="M535 0 L548 0 C520 140 550 280 616 411 L600 411 C535 280 505 140 535 0 Z" fill="var(--red-dark)"/>
    <path d="M548 0 L575 0 C545 150 575 285 650 411 L616 411 C550 280 520 140 548 0 Z" fill="var(--silver-light)"/>
    <rect x="0" y="0" width="720" height="14" fill="var(--silver)"/>
    <rect x="0" y="397" width="720" height="14" fill="var(--silver)"/>
  </svg>

  <h1 class="holder-name">Teodor K (Ted)</h1>
  <div class="rule" style="top:76px"></div>
  <ul class="services">
    <li>Repairs, Installations, and Maintenance</li>
    <li>Quality work at reasonable prices</li>
    <li>Residential / Commercial</li>
    <li>Licensed &amp; Insured</li>
  </ul>
  <div class="rule" style="top:200px"></div>

  <p class="contact contact-phone">
    <svg viewBox="0 0 24 24" aria-hidden="true"><rect x="6" y="2" width="12" height="20" rx="2" fill="var(--red)"/><rect x="8" y="5" width="8" height="11" fill="var(--white)"/><circle cx="12" cy="19" r="1.2" fill="var(--white)"/></svg>
    555.284.9137
  </p>
  <div class="rule" style="top:256px"></div>
  <p class="contact contact-email">
    <svg viewBox="0 0 24 24" aria-hidden="true"><rect x="2" y="5" width="20" height="14" rx="2" fill="var(--red)"/><path d="M3 6 L12 13 L21 6" stroke="var(--white)" stroke-width="1.8" fill="none"/></svg>
    Pinegrovehvac47@mailbox-example.com
  </p>
  <div class="rule" style="top:312px"></div>

  <div class="photo photo-repair" role="img" aria-label="Photo of a technician repairing an air conditioning unit"></div>
  <div class="photo photo-unit" role="img" aria-label="Photo of a hand holding a remote in front of a wall air conditioner"></div>

  <div class="front-logo"><span class="mark"></span><span class="brand-name">PINEGROVE</span></div>
</section>

</body>
</html>
```